Wedding Invitation and envelope package

I need the 1st of many invitation designs. This is a floral collection and I have attached many designs that I like from competitors. I think that the pastel look is the best but I am hoping you can make something special. The font selection is just as important as the imagery. The overall size with bleeds is 5.25 x 7.25" and I have attached a sample to make sure sizing is clear. I also need A7 envelopes to go with the invitation, front and back flap. I want someone to look at the design and say they would pick it over any of the samples. I will need 8 total floral designs done over the next few weeks after this 1st one is done. I will also need a collection of 8 modern designs done. Please ask any questions

Font styles to use
Serif
Sans Serif
Script

Requirements
Must have
• This is a single sided invitation, a back side is not needed.
Should not have
• No full solid dark backgrounds

```html
<!DOCTYPE html>
<html lang="en">
<head>
<meta charset="utf-8">
<title>Floral Wedding Invitation and A7 Envelope Set</title>
<link href="https://fonts.googleapis.com/css2?family=Allura&family=Playfair+Display:wght@400&family=La+Belle+Aurore&display=swap" rel="stylesheet">
<style>
  :root {
    --backdrop: #ecebe9;
    --paper: #ffffff;
    --paper-shade: #f2f2f1;
    --floral-pale: #f6f7dc;
    --floral-mid: #eef0b8;
    --floral-grey: #e6e6e6;
    --ink: #2b2a2a;
    --rule: #b5b5b5;
    --accent-red: #d01f1f;
    --frame-peach: #f0a27a;
  }
  * { margin: 0; padding: 0; box-sizing: border-box; }
  html, body { width: 1200px; height: 657px; overflow: hidden; }
  body { background: var(--backdrop); position: relative; font-family: "Playfair Display", Georgia, serif; color: var(--ink); }

  .invitation {
    position: absolute; left: 62px; top: 53px; width: 407px; height: 556px;
    box-shadow: 0 4px 14px rgba(0,0,0,.12);
  }
  .floral-field {
    position: absolute; inset: 0;
    background:
      radial-gradient(circle at 20% 20%, var(--floral-mid) 0, transparent 30%),
      radial-gradient(circle at 85% 70%, var(--floral-mid) 0, transparent 28%),
      radial-gradient(circle at 10% 75%, var(--floral-mid) 0, transparent 25%),
      linear-gradient(160deg, var(--floral-pale), var(--floral-grey) 55%, var(--floral-pale));
  }
  .content-panel { position: absolute; left: 37px; top: 49px; width: 334px; height: 458px; }
  .content-panel svg { position: absolute; inset: 0; }

  .centered { position: absolute; left: 0; width: 407px; text-align: center; }
  .intro { top: 76px; font-size: 11px; line-height: 17px; }
  .couple-first, .couple-second { position: absolute; font-family: "Allura", cursive; font-size: 78px; line-height: 1; }
  .couple-first { left: 98px; top: 140px; }
  .couple-second { left: 178px; top: 222px; }
  .hearts { position: absolute; left: 186px; top: 205px; }

  .date-block { position: absolute; top: 312px; left: 86px; width: 237px; height: 60px; }
  .date-rule-group { position: absolute; top: 12px; width: 93px; height: 25px; border-top: 1.5px solid var(--rule); border-bottom: 1.5px solid var(--rule); font-size: 9.5px; letter-spacing: 3px; text-align: center; line-height: 22px; }
  .day { left: 0; }
  .time { right: 0; }
  .month, .year { position: absolute; left: 0; width: 237px; text-align: center; font-size: 9.5px; letter-spacing: 3px; }
  .month { top: 0; }
  .year { top: 46px; }
  .day-number { position: absolute; left: 0; width: 237px; top: 12px; text-align: center; font-size: 25px; line-height: 1; }

  .details { top: 372px; font-size: 11px; line-height: 14px; }
  .accent-line { top: 410px; font-family: "La Belle Aurore", cursive; font-size: 22px; color: var(--accent-red); }
  .closing { top: 449px; font-size: 11px; line-height: 14px; }

  .envelope-back { position: absolute; left: 530px; top: 36px; width: 390px; height: 262px; background: var(--paper-shade); box-shadow: 0 3px 10px rgba(0,0,0,.1); }
  .envelope-back svg { position: absolute; inset: 0; }
  .flap-monogram { position: absolute; left: 0; width: 390px; top: 70px; text-align: center; font-family: "Allura", cursive; font-size: 34px; }

  .envelope-front { position: absolute; left: 713px; top: 312px; width: 429px; height: 312px; background: var(--paper-shade); box-shadow: 0 3px 10px rgba(0,0,0,.1); }
  .front-floral-band { position: absolute; left: 0; top: 0; width: 429px; height: 130px; background: linear-gradient(180deg, var(--floral-mid), var(--floral-pale) 55%, var(--paper-shade)); }
  .front-name-first, .front-name-second { position: absolute; font-family: "Allura", cursive; font-size: 58px; line-height: 1; }
  .front-name-first { left: 138px; top: 128px; }
  .front-name-second { left: 196px; top: 184px; }
  .front-hearts { position: absolute; left: 205px; top: 176px; }
  .front-note { position: absolute; left: 0; width: 429px; top: 248px; text-align: center; font-size: 9.5px; line-height: 12px; }
</style>
</head>
<body>

<section class="invitation">
  <div class="floral-field" role="img" aria-label="Pastel yellow paper flower pattern on a soft grey ground"></div>
  <div class="content-panel">
    <svg width="334" height="458" viewBox="0 0 334 458">
      <path d="M0.5 0.5 H279 A55 55 0 0 0 333.5 56 V457.5 H0.5 Z" fill="var(--paper)" stroke="var(--frame-peach)" stroke-width="1"/>
    </svg>
  </div>

  <p class="centered intro">Lorem Ipsum is simply dummy<br>text of the printing and typesetting industry.<br>standard dummy text ever since the 1500s,</p>

  <div class="couple-first">Lorem</div>
  <svg class="hearts" width="34" height="18" viewBox="0 0 34 18" fill="none" stroke="var(--accent-red)" stroke-width="1.4">
    <path d="M9 16 C1 10 1 4 5 3 C8 2 9 5 9 6 C9 5 11 2 14 3 C17 5 15 11 9 16Z"/>
    <path d="M24 15 C18 10 18 5 21 4 C23 3.5 24 5.5 24 6 C24 5.5 26 3 28 4 C31 6 29 10 24 15Z"/>
  </svg>
  <div class="couple-second">Ipsum</div>

  <div class="date-block">
    <div class="month">SEP</div>
    <div class="date-rule-group day">SATURDAY</div>
    <div class="day-number">20</div>
    <div class="date-rule-group time">02:00 PM</div>
    <div class="year">2020</div>
  </div>

  <p class="centered details">Lorem Ipsum is simply dummy text of the printing and<br>typesetting industry. &nbsp;standard dummy text ever since the 1500s,</p>
  <p class="centered accent-line">Lorem Ipsum is dummy text</p>
  <p class="centered closing">Lorem Ipsum is simply dummy text of the<br>printing and typesetting industry.</p>
</section>

<section class="envelope-back">
  <svg width="390" height="262" viewBox="0 0 390 262">
    <defs>
      <linearGradient id="flapFloral" x1="0" y1="0" x2="0" y2="1">
        <stop offset="0" stop-color="#eef0b8"/>
        <stop offset="1" stop-color="#f6f7dc"/>
      </linearGradient>
    </defs>
    <path d="M0 0 H390 L240 150 Q195 185 150 150 Z" fill="url(#flapFloral)" stroke="#dcdcdc" stroke-width="1" role="img" aria-label="Back flap covered in pastel yellow paper flower pattern"/>
  </svg>
  <div class="flap-monogram">Lorem &amp; Ipsum</div>
</section>

<section class="envelope-front">
  <div class="front-floral-band" role="img" aria-label="Pastel yellow paper flower border fading into the envelope"></div>
  <div class="front-name-first">Lorem</div>
  <svg class="front-hearts" width="26" height="14" viewBox="0 0 34 18" fill="none" stroke="var(--accent-red)" stroke-width="1.6">
    <path d="M9 16 C1 10 1 4 5 3 C8 2 9 5 9 6 C9 5 11 2 14 3 C17 5 15 11 9 16Z"/>
    <path d="M24 15 C18 10 18 5 21 4 C23 3.5 24 5.5 24 6 C24 5.5 26 3 28 4 C31 6 29 10 24 15Z"/>
  </svg>
  <div class="front-name-second">Ipsum</div>
  <p class="front-note">Lorem Ipsum is simply dummy text of the<br>printing and typesetting industry.</p>
</section>

</body>
</html>
```